Personal sales brochure for client marketing

I am looking for a brochure in the style of a sales menu to sit in front of clients with. I want 5 different colored columns where clients will choose the right package for them.
Eg.
Package 1 called Book-keeping is a basic package
Package 2 called Insight includes the above but also extra services
Package 3 called Compliance an add on for the above packages
Package 4 Called Professional another add on to the above services
Package 5 called payroll another add on to the above.

I want to sit in front of my clients and discuss the services we provide and allow them to choose from this list and tick the boxes of what they would like. I attach a simple spread sheet as well for guideline.

Target Market(s)

business owners requiring accounting support and advice

Industry/Entity Type

Accounting

Font styles to use
Serif
Sans Serif

Requirements
Must have
• Simple, clear, concise with clear product descriptions in colored boxes that highlight clearly the different options. Must have Logo and contact details. This document need to be our key sales and marketing tool so will need to introduce the business clearly and in a professional manner.
• enquiries@brantwellpartners.gg
• 01481 439216
Nice to have
• The design needs to be printable on A1 A3 A4 A5
Should not have
• Pictures and patterns

```html
<!DOCTYPE html>
<html lang="en">
<head>
<meta charset="utf-8">
<title>Brantwell Partners – Service Menu</title>
<link rel="stylesheet" href="https://fonts.googleapis.com/css2?family=Open+Sans:ital,wght@0,300;0,400;1,300&display=swap">
<style>
  :root {
    --paper: #ffffff;
    --ink: #3a3f3e;
    --brand-grey: #6d7170;
    --contact-grey: #7f8a88;
    --payroll: #e3e8e7;
    --payroll-band: #d8dfdd;
    --bookkeeping: #bccac7;
    --bookkeeping-band: #c4cecb;
    --insight: #98aba7;
    --insight-band: #9fb1ad;
    --compliance: #6f8683;
    --compliance-band: #718784;
    --professional: #4c5c5a;
    --professional-band: #4f5f5d;
    --light-text: #ffffff;
  }
  * { margin: 0; padding: 0; box-sizing: border-box; }
  html, body { width: 1200px; height: 848px; overflow: hidden; background: var(--paper); }
  body { font-family: "Open Sans", Arial, sans-serif; color: var(--ink); }

  .brochure { position: relative; width: 1200px; height: 848px; overflow: hidden; }

  .brand { position: absolute; left: 404px; top: 54px; width: 380px; text-align: center; color: var(--brand-grey); }
  .brand-name { font-weight: 300; font-size: 38px; line-height: 1; letter-spacing: 0.5px; }
  .brand-tagline { margin-top: 12px; font-size: 13px; font-weight: 300; letter-spacing: 0.5px; }

  .contact { position: absolute; left: 852px; top: 52px; color: var(--contact-grey); }
  .contact-email { font-size: 17px; font-weight: 300; }
  .contact-phone { font-size: 30px; font-weight: 300; margin-top: 2px; letter-spacing: 0.5px; }

  .packages { position: absolute; left: 14px; top: 185px; display: flex; gap: 11px; }
  .package { width: 226px; }
  .package-band { height: 20px; }
  .package-body { margin-top: 13px; height: 650px; padding: 32px 26px 0 12px; color: var(--light-text); }
  .package-title { text-align: center; font-style: italic; font-weight: 300; font-size: 25px; margin: 0 -14px 34px 0; }
  .package-list { list-style: none; font-size: 13px; line-height: 18px; font-weight: 400; }
  .package-list li { margin-bottom: 20px; }

  .payroll .package-band { background: var(--payroll-band); }
  .payroll .package-body { background: var(--payroll); color: var(--ink); }
  .bookkeeping .package-band { background: var(--bookkeeping-band); }
  .bookkeeping .package-body { background: var(--bookkeeping); }
  .insight .package-band { background: var(--insight-band); }
  .insight .package-body { background: var(--insight); }
  .compliance .package-band { background: var(--compliance-band); }
  .compliance .package-body { background: var(--compliance); }
  .professional .package-band { background: var(--professional-band); }
  .professional .package-body { background: var(--professional); }
</style>
</head>
<body>
<main class="brochure">
  <header>
    <div class="brand">
      <div class="brand-name">Brantwell Partners</div>
      <div class="brand-tagline">Accounting and business solutions</div>
    </div>
    <div class="contact">
      <div class="contact-email">enquiries@brantwellpartners.gg</div>
      <div class="contact-phone">01481 439216</div>
    </div>
  </header>

  <section class="packages">
    <article class="package payroll">
      <div class="package-band"></div>
      <div class="package-body">
        <h2 class="package-title">Payroll</h2>
        <ul class="package-list">
          <li>Weekly/monthly</li>
          <li>ETI Returns</li>
          <li>UK/Channel Islands</li>
        </ul>
      </div>
    </article>

    <article class="package bookkeeping">
      <div class="package-band"></div>
      <div class="package-body">
        <h2 class="package-title">Book Keeping</h2>
        <ul class="package-list">
          <li>Monthly/Quarterly/Annually</li>
          <li>Invoices entered and bank accounts reconciled.</li>
          <li>Purchase and sales ledgers reconciled.</li>
          <li>All software is included.</li>
          <li>Unlimited support and assistance.</li>
        </ul>
      </div>
    </article>

    <article class="package insight">
      <div class="package-band"></div>
      <div class="package-body">
        <h2 class="package-title">Insight</h2>
        <ul class="package-list">
          <li>Monthly/Quarterly/Annually</li>
          <li>Invoices entered and bank accounts reconciled.</li>
          <li>Purchase and sales ledgers reconciled.</li>
          <li>Accounting adjustments to give a true reflection of your profit/loss to date.</li>
          <li>Management Accounts.</li>
          <li>Regular meeting to discuss business performance and possible areas for improvement.</li>
          <li>All software is included.</li>
          <li>Unlimited support and assistance.</li>
        </ul>
      </div>
    </article>

    <article class="package compliance">
      <div class="package-band"></div>
      <div class="package-body">
        <h2 class="package-title">Compliance</h2>
        <ul class="package-list">
          <li>What every business must do:</li>
          <li>Financial statements prepared</li>
          <li>Income tax computation</li>
          <li>Personal tax returns</li>
          <li>All software is included.</li>
          <li>Unlimited support and assistance.</li>
        </ul>
      </div>
    </article>

    <article class="package professional">
      <div class="package-band"></div>
      <div class="package-body">
        <h2 class="package-title">Professional</h2>
        <ul class="package-list">
          <li>Bespoke solutions for your business.</li>
          <li>Business planning</li>
          <li>Cash flow planning and forecasting.</li>
          <li>Specialist tax planning.</li>
          <li>Business turnaround.</li>
          <li>All software is included.</li>
          <li>Unlimited support and assistance.</li>
        </ul>
      </div>
    </article>
  </section>
</main>
</body>
</html>
```